BRISK Study flyer

I need help designing a flyer for a research study that will include brain imaging in adolescents. The info is in the attached document. The study is called the Brain Rhythms In School Kids (BRISK) study. Ideally this would be returned as a document that I can edit in the future as we will have several new recruitment phases (different age groups, etc. I also would love to have a logo designed as part of this project, but I recognize that might be a separate design request.

```html
<!DOCTYPE html>
<html lang="en">
<head>
<meta charset="utf-8">
<title>BRISK Study Flyer</title>
<link rel="stylesheet" href="https://fonts.googleapis.com/css2?family=Alegreya+SC:ital,wght@1,700&family=Cinzel:wght@500&family=Great+Vibes&family=Poppins:wght@300;400;600;700&display=swap">
<style>
  :root {
    --page-bg: #b9b9b9;
    --white: #ffffff;
    --hero-bg: #f0f1f6;
    --teal: #00868f;
    --teal-deep: #00636b;
    --teal-title: #0d6a70;
    --ink: #1c1c1c;
    --pill: #00858e;
    --pill-glow: #1bb7c4;
  }
  * { box-sizing: border-box; margin: 0; padding: 0; }
  html, body { width: 984px; height: 1200px; overflow: hidden; }
  body { background: var(--page-bg); font-family: "Poppins", sans-serif; position: relative; }

  .flyer { position: absolute; left: 160px; top: 102px; width: 664px; height: 995px; background: var(--white); overflow: hidden; }

  .study-title {
    position: absolute; left: 0; top: 18px; width: 100%; text-align: center;
    font-family: "Cinzel", serif; font-weight: 500; font-size: 21px; line-height: 30px;
    color: var(--teal-title); letter-spacing: 0.3px;
  }

  .hero { position: absolute; left: 0; top: 86px; width: 664px; height: 308px; background: var(--hero-bg); }
  .hero-photo {
    position: absolute; right: 0; top: 0; width: 330px; height: 308px;
    background: linear-gradient(100deg, var(--hero-bg) 0%, #e7d6c8 22%, #caa889 48%, #3a3f4a 62%, #b98a5e 80%, #8a5d38 100%);
  }
  .hero-question {
    position: absolute; left: 0; top: 34px; width: 360px;
    font-family: "Great Vibes", cursive; font-size: 40px; line-height: 44px; color: var(--ink); white-space: nowrap;
  }
  .age-pill {
    position: absolute; left: 55px; top: 89px; width: 245px; height: 94px; border-radius: 30px;
    background: var(--pill); box-shadow: inset 0 0 10px var(--pill-glow), 0 0 0 2px var(--pill-glow);
    display: flex; align-items: center; justify-content: center;
    color: var(--white); font-weight: 700; font-size: 40px; letter-spacing: -0.5px;
  }
  .hero-subline {
    position: absolute; left: 10px; top: 204px; width: 335px; text-align: center;
    font-weight: 600; font-size: 19px; line-height: 30px; color: var(--ink);
  }

  .details { position: absolute; left: 0; top: 394px; width: 664px; height: 484px; background: var(--teal); color: var(--white); }
  .involvement { position: absolute; left: 30px; top: 51px; width: 610px; height: 268px; background: var(--teal-deep); border-radius: 30px; }
  .involvement-lead {
    position: absolute; left: 10px; top: 16px; width: 590px; text-align: center;
    font-weight: 600; font-size: 12px; line-height: 22px; text-transform: uppercase;
  }
  .bullet-list { list-style: none; position: absolute; }
  .bullet-list li { position: relative; padding-left: 24px; font-size: 12.5px; line-height: 16px; font-weight: 400; }
  .bullet-list li svg { position: absolute; left: 0; top: 1px; width: 18px; height: 14px; }
  .involvement .bullet-list { left: 42px; top: 105px; width: 500px; }
  .involvement .bullet-list li { margin-bottom: 14px; }

  .eligibility-heading { position: absolute; left: 0; top: 349px; width: 626px; text-align: center; font-weight: 600; font-size: 15px; }
  .eligibility .bullet-list { left: 72px; top: 378px; width: 540px; }
  .eligibility .bullet-list li { margin-bottom: 14px; }

  .contact-strip {
    position: absolute; left: 0; top: 878px; width: 664px; height: 54px; background: var(--white);
    display: flex; align-items: center; justify-content: center; gap: 5px; white-space: nowrap;
  }
  .contact-strip .ask { font-family: "Alegreya SC", serif; font-style: italic; font-weight: 700; font-size: 16px; color: var(--ink); }
  .contact-strip .more { font-weight: 700; font-size: 19px; color: var(--teal); }

  .footer { position: absolute; left: 0; top: 932px; width: 664px; height: 63px; background: var(--teal); color: var(--white); }
  .footer .email { position: absolute; left: 28px; top: 19px; font-weight: 300; font-size: 16px; }
  .footer .compensation { position: absolute; right: 26px; top: 12px; font-weight: 700; font-size: 20px; }
</style>
</head>
<body>
<svg width="0" height="0" style="position:absolute">
  <defs>
    <symbol id="diamond-bullet" viewBox="0 0 18 14">
      <path d="M7 1 L13 7 L7 13 L1 7 Z" fill="none" stroke="#ffffff" stroke-width="1"/>
      <path d="M7 4 L10 7 L7 10 L4 7 Z" fill="#ffffff"/>
      <path d="M11 2 L16 7 L11 12" fill="none" stroke="#ffffff" stroke-width="1"/>
    </symbol>
  </defs>
</svg>

<main class="flyer">
  <h1 class="study-title">Brain Rhythms In School<br>Kids</h1>

  <section class="hero">
    <div class="hero-photo" role="img" aria-label="Photo of a smiling child playing with a stack of wooden blocks"></div>
    <p class="hero-question">Are you the Parent of a Child</p>
    <div class="age-pill">Age 10-17?</div>
    <p class="hero-subline">DO THEY WORRY OR OVERTHINK NEGATIVE EMOTIONS?</p>
  </section>

  <section class="details">
    <div class="involvement">
      <p class="involvement-lead">Northvale University researchers are seeking girls age 10-17 for a study about brain activity in emotions and decision-making and how they relate to puberty, anxiety and depression. Study participation involves:</p>
      <ul class="bullet-list">
        <li><svg><use href="#diamond-bullet"/></svg>One one-hour interview (online or in-person) where your child will discuss their thoughts</li>
        <li><svg><use href="#diamond-bullet"/></svg>Online questionnaires (parent and child)</li>
        <li><svg><use href="#diamond-bullet"/></svg>One two-hour visit where your child will complete an MRI scan, answer questions about their puberty stage, and have a small hair sample taken to study puberty hormones</li>
      </ul>
    </div>

    <div class="eligibility">
      <h2 class="eligibility-heading">YOUR CHILD MAY BE ELIGIBLE IF THEY</h2>
      <ul class="bullet-list">
        <li><svg><use href="#diamond-bullet"/></svg>Are age 10-17</li>
        <li><svg><use href="#diamond-bullet"/></svg>Tend to worry or overthink negative thoughts</li>
        <li><svg><use href="#diamond-bullet"/></svg>Have not been diagnosed with psychosis, learning problems, or autism</li>
      </ul>
    </div>
  </section>

  <div class="contact-strip">
    <span class="ask">Interested in participating?</span>
    <span class="more">Want more information?</span>
    <span class="ask">Please contact us!</span>
  </div>

  <footer class="footer">
    <span class="email">briskstudy@northvale.edu</span>
    <span class="compensation">Compensation up to $140</span>
  </footer>
</main>
</body>
</html>
```